Quorbix new startup tech website refresh

We need a new website design for a tech startup company. We want a cutting edge high tech looking website. See quorbix-example.com for the current site that needs to be updated with a fresh look. Use the info from the website.
We want the site to feel fast, sleek, and tech-driven while still speaking directly to the customers who will use Quorbix. The design should highlight speed, efficiency, and precision with a monospace code font for headlines, stats, and technical details, paired with a clean sans-serif for body copy. This reinforces the product’s engineering credibility while keeping content easy to read.

Target Market(s)

tech Enterprises, Start up companies and Cloud providers

Industry/Entity Type

Tech

Number of Pages Required

2 page

Requirements
Must have
• We want the site to feel fast, sleek, and tech-driven while still speaking directly to the customers who will use Quorbix. The design should highlight speed, efficiency, and precision with a monospace code font for headlines, stats, and technical details, paired with a clean sans-serif for body copy. This reinforces the product’s engineering credibility while keeping content easy to read.

```html
<!DOCTYPE html>
<html lang="en">
<head>
<meta charset="utf-8">
<title>Quorbix — Accelerate Your Data</title>
<link rel="stylesheet" href="https://fonts.googleapis.com/css2?family=IBM+Plex+Mono:wght@400;500;600&family=Inter:wght@400;500;600&display=swap">
<style>
  :root {
    --bg: #161b24;
    --bg-deep: #11151d;
    --line: #2a303b;
    --card-border: #343a46;
    --text: #f1f3f7;
    --text-soft: #c9ced8;
    --text-muted: #8f96a3;
    --accent-violet: #8b3fe0;
    --accent-blue: #2f5fe0;
    --glow-cyan: #3aa8ff;
    --glow-purple: #7a3cf0;
  }
  * { box-sizing: border-box; margin: 0; padding: 0; }
  html, body { width: 1200px; height: 1076px; overflow: hidden; background: var(--bg); }
  body { position: relative; font-family: "Inter", sans-serif; color: var(--text); }

  .site-header { position: absolute; left: 0; top: 0; width: 1200px; height: 102px; border-bottom: 1px solid var(--line); background: var(--bg); }
  .brand { position: absolute; left: 113px; top: 34px; display: flex; align-items: center; gap: 10px; font-family: "IBM Plex Mono", monospace; font-weight: 600; font-size: 28px; color: var(--text); }
  .brand-mark { width: 10px; height: 10px; background: var(--text); }
  .main-nav { position: absolute; top: 38px; left: 498px; font-size: 17px; color: var(--text-soft); }
  .main-nav a { position: absolute; white-space: nowrap; color: inherit; text-decoration: none; }
  .main-nav .active::after { content: ""; position: absolute; left: -14px; right: -14px; top: 42px; height: 3px; background: var(--accent-violet); border-radius: 2px; }
  .demo-button { position: absolute; left: 946px; top: 32px; width: 137px; height: 40px; border-radius: 7px; background: linear-gradient(90deg, var(--accent-blue), var(--accent-violet)); color: #fff; font-size: 16px; font-weight: 500; display: flex; align-items: center; justify-content: center; }

  .hero { position: absolute; left: 0; top: 103px; width: 1200px; height: 367px; background: var(--bg); }
  .hero-visual { position: absolute; right: 0; top: 0; width: 500px; height: 367px; background: radial-gradient(circle at 58% 44%, rgba(58,168,255,0.55) 0, rgba(122,60,240,0.35) 22%, rgba(40,30,90,0.3) 42%, rgba(17,21,29,0.6) 68%, var(--bg) 100%); }
  .hero-title { position: absolute; left: 110px; top: 108px; font-family: "IBM Plex Mono", monospace; font-weight: 600; font-size: 46px; line-height: 60px; letter-spacing: 0.3px; white-space: nowrap; }
  .hero-lede { position: absolute; left: 110px; top: 250px; font-size: 21px; line-height: 31px; color: var(--text-soft); }

  .section-title { position: absolute; left: 113px; font-size: 26px; font-weight: 600; color: var(--text); }
  .features-title { top: 512px; }
  .feature-card { position: absolute; top: 567px; height: 178px; border: 1px solid var(--card-border); border-radius: 6px; padding: 26px 16px 0 52px; }
  .feature-card h3 { font-family: "IBM Plex Mono", monospace; font-weight: 500; font-size: 24px; letter-spacing: 0.5px; margin-bottom: 22px; }
  .feature-card ul { list-style: none; font-family: "IBM Plex Mono", monospace; font-size: 15px; color: var(--text-muted); }
  .feature-card li { position: relative; line-height: 24px; margin-bottom: 22px; white-space: nowrap; }
  .feature-card li::before { content: ""; position: absolute; left: -16px; top: 11px; width: 4px; height: 4px; border-radius: 50%; background: var(--text-muted); }
  .feature-card .compact li { margin-bottom: 0; }
  .card-speed { left: 117px; width: 301px; }
  .card-efficiency { left: 452px; width: 296px; padding-left: 52px; }
  .card-precision { left: 778px; width: 304px; padding-left: 53px; }

  .platform-title { top: 800px; }
  .platform-visual { position: absolute; left: 125px; top: 858px; width: 217px; height: 97px; border-radius: 48px; background: radial-gradient(ellipse at center, rgba(122,60,240,0.45) 0, rgba(47,95,224,0.25) 45%, transparent 75%); }
  .stat { position: absolute; top: 864px; }
  .stat-value { font-family: "IBM Plex Mono", monospace; font-weight: 600; font-size: 29px; line-height: 36px; white-space: nowrap; }
  .stat-value small { font-family: "Inter", sans-serif; font-weight: 500; font-size: 25px; }
  .stat-label { font-size: 19px; color: var(--text-muted); margin-top: 6px; }
  .stat-label.mono { font-family: "IBM Plex Mono", monospace; }
  .stat-uptime { left: 398px; }
  .stat-queries { left: 678px; }
  .stat-speed { left: 895px; }
  .stat-divider { position: absolute; top: 860px; width: 1px; height: 94px; background: var(--line); }

  .site-footer { position: absolute; left: 0; top: 983px; width: 1200px; height: 93px; border-top: 1px solid var(--line); }
  .footer-brand { top: 32px; left: 118px; }
  .social-links { position: absolute; left: 630px; top: 38px; display: flex; gap: 12px; }
  .social-links span { width: 16px; height: 16px; border-radius: 50%; border: 2px solid var(--text-muted); }
  .footer-divider { position: absolute; left: 822px; top: 28px; width: 1px; height: 36px; background: var(--line); }
  .footer-badge { position: absolute; left: 850px; top: 37px; width: 18px; height: 18px; border-radius: 50%; background: var(--text-muted); }
  .footer-contact { position: absolute; left: 902px; top: 22px; font-size: 12px; line-height: 16px; color: var(--text-muted); white-space: nowrap; font-style: normal; text-align: center; }
</style>
</head>
<body>
  <header class="site-header">
    <div class="brand"><span class="brand-mark"></span>Quorbix</div>
    <nav class="main-nav">
      <a class="active" style="left:0">Solutions</a>
      <a style="left:120px">Platform</a>
      <a style="left:234px">About Us</a>
      <a style="left:345px">Careers</a>
    </nav>
    <div class="demo-button">Request Demo</div>
  </header>

  <section class="hero">
    <div class="hero-visual" role="img" aria-label="Glowing blue and purple network sphere of connected data nodes"></div>
    <h1 class="hero-title">Accelerate Your Data.<br>Instantly.</h1>
    <p class="hero-lede">Unleash the power of real-time data processing for<br>enterprises and cloud providers.</p>
  </section>

  <h2 class="section-title features-title">Features</h2>
  <article class="feature-card card-speed">
    <h3>SPEED</h3>
    <ul><li>Sub-millisecond latency</li><li>Error-free pipelines</li></ul>
  </article>
  <article class="feature-card card-efficiency">
    <h3>EFFICIENCY</h3>
    <ul class="compact"><li>Automated workflows</li><li>Smart resource use</li><li>Cost optimization</li></ul>
  </article>
  <article class="feature-card card-precision">
    <h3>PRECISION</h3>
    <ul><li>Error-free pipelines</li></ul>
  </article>

  <h2 class="section-title platform-title">Our Platform</h2>
  <div class="platform-visual" role="img" aria-label="Small network diagram of connected purple and blue nodes"></div>
  <div class="stat stat-uptime"><div class="stat-value">99.999% <small>Uptime</small></div><div class="stat-label">Uptime</div></div>
  <div class="stat-divider" style="left:647px"></div>
  <div class="stat stat-queries"><div class="stat-value">10M+</div><div class="stat-label mono">Queries/Sec</div></div>
  <div class="stat-divider" style="left:862px"></div>
  <div class="stat stat-speed"><div class="stat-value">500x <small>Faster</small></div><div class="stat-label">Faster</div></div>

  <footer class="site-footer">
    <div class="brand footer-brand"><span class="brand-mark"></span>Quorbix</div>
    <div class="social-links" aria-label="Social links"><span></span><span></span><span></span><span></span><span></span><span></span></div>
    <div class="footer-divider"></div>
    <div class="footer-badge"></div>
    <address class="footer-contact">Headquarters location<br>+1 000 000 0000<br>hello@quorbix-example.com</address>
  </footer>
</body>
</html>
```